Merchandising Kaffeebohnen mit Firmen Branding
Zielgruppe
Willkommen bei KLV Talmetall, Ihrem internationalen Experten für smarte Recycling- und Verwertungslösungen in der Elektronikbranche. Wir steigern die nachhaltige und wirtschaftliche Performance Ihres Unternehmens mit maßgeschneiderten und CO2-reduzierenden Recyclinglösungen für Lötzinn und edelmetallhaltige Produktionsabfälle. Mit unserer proaktiven Beratung helfen wir Ihrem Unternehmen, nicht nur umweltfreundlich zu agieren, sondern leisten einen messbaren Beitrag für eine zukunftsorientierte Marktpositionierung!
Aufgabenstellung
Modern & schlicht
Wir haben eine Espresso Event und dazu unseren eigenen Kaffee und dafür benötigen wir ein Design.

```html
<!DOCTYPE html>
<html lang="de">
<head>
<meta charset="utf-8">
<title>KLV Talmetall – Espresso Ganze Bohne</title>
<link rel="stylesheet" href="https://fonts.googleapis.com/css2?family=Montserrat:wght@700;800&family=Raleway:wght@300;400&display=swap">
<style>
  :root {
    --stage: #5e5e5e;
    --bag-black: #1b1b1b;
    --gold: #b49b5e;
    --gold-light: #cdb577;
    --gold-dark: #8f7a44;
    --white: #ffffff;
    --ink: #2a2414;
  }
  * { box-sizing: border-box; margin: 0; padding: 0; }
  html, body { width: 1200px; height: 2400px; overflow: hidden; }
  body { background: var(--stage); font-family: "Raleway", sans-serif; }

  .variant { position: relative; width: 1200px; height: 1200px; }

  .bag { position: absolute; left: 294px; top: 140px; display: flex; height: 960px; }

  .front {
    position: relative; width: 489px; height: 100%;
    background: var(--bag-black); color: var(--gold);
    text-align: center;
  }
  .brand {
    position: absolute; top: 120px; left: 0; right: 0;
    display: flex; align-items: center; justify-content: center; gap: 14px;
    font-family: "Montserrat", sans-serif; font-weight: 700;
    font-size: 34px; line-height: 40px; color: var(--white); letter-spacing: 1px;
  }
  .brand-square { width: 22px; height: 22px; background: var(--white); flex: none; }

  .title {
    position: absolute; top: 412px; left: 0; right: 0;
    font-family: "Montserrat", sans-serif; font-weight: 800;
    font-size: 70px; letter-spacing: 1px; line-height: 70px;
  }
  .subtitle {
    position: absolute; top: 496px; left: 0; right: 0;
    font-weight: 300; font-size: 42px; line-height: 42px;
  }
  .strength { position: absolute; left: 0; right: 0; margin: 0 auto; display: block; }
  .front .strength { top: 556px; }

  .pattern-band { position: absolute; left: 0; right: 0; top: 605px; height: 252px; }
  .variant--flat .pattern-band {
    background: linear-gradient(90deg, #3a3322 0%, #6e5f38 30%, #3a3322 55%, #6e5f38 80%, #3a3322 100%);
  }
  .variant--metallic .pattern-band {
    background: linear-gradient(180deg, #6e6a60 0%, #7a6a3e 45%, #3a3322 80%, var(--bag-black) 100%);
  }

  .weight {
    position: absolute; top: 867px; left: 0; right: 0;
    font-weight: 300; font-size: 34px; line-height: 36px;
  }

  .gusset {
    position: relative; width: 121px; height: 100%;
    background: linear-gradient(90deg, var(--gold-dark), var(--gold-light) 40%, var(--gold) 100%);
    color: var(--ink); text-align: center;
  }
  .gusset .brand {
    top: 440px; font-size: 13px; line-height: 16px; gap: 6px; flex-direction: column; letter-spacing: 0;
  }
  .gusset .brand-square { width: 12px; height: 12px; }
  .gusset-title {
    position: absolute; top: 566px; left: 0; right: 0;
    font-family: "Montserrat", sans-serif; font-weight: 800; font-size: 19px; line-height: 22px;
  }
  .gusset-subtitle {
    position: absolute; top: 592px; left: 0; right: 0;
    font-weight: 300; font-size: 13px; line-height: 15px;
  }
  .gusset .strength { top: 614px; }
  .gusset-copy {
    position: absolute; top: 640px; left: 10px; right: 10px;
    font-size: 8.5px; line-height: 1.55; text-align: left; hyphens: auto;
  }
</style>
</head>
<body>

<section class="variant variant--flat">
  <div class="bag">
    <div class="front">
      <div class="brand"><span class="brand-square"></span>KLV Talmetall</div>
      <h1 class="title">ESPRESSO</h1>
      <p class="subtitle">GANZE BOHNE</p>
      <svg class="strength" width="130" height="28" viewBox="0 0 130 28" aria-label="Stärke 3 von 5">
        <ellipse cx="13" cy="14" rx="9" ry="13" fill="var(--gold)"/>
        <ellipse cx="39" cy="14" rx="9" ry="13" fill="var(--gold)"/>
        <ellipse cx="65" cy="14" rx="9" ry="13" fill="var(--gold)"/>
        <ellipse cx="91" cy="14" rx="9" ry="13" fill="var(--white)"/>
        <ellipse cx="117" cy="14" rx="9" ry="13" fill="var(--white)"/>
      </svg>
      <div class="pattern-band" role="img" aria-label="Wabenmuster aus goldenen und weißen Sechsecken"></div>
      <p class="weight">250g</p>
    </div>
    <div class="gusset">
      <div class="brand"><span class="brand-square"></span>KLV Talmetall</div>
      <p class="gusset-title">ESPRESSO</p>
      <p class="gusset-subtitle">GANZE BOHNE</p>
      <svg class="strength" width="50" height="12" viewBox="0 0 60 14" aria-label="Stärke 3 von 5">
        <ellipse cx="6" cy="7" rx="4.5" ry="6.5" fill="var(--ink)"/>
        <ellipse cx="18" cy="7" rx="4.5" ry="6.5" fill="var(--ink)"/>
        <ellipse cx="30" cy="7" rx="4.5" ry="6.5" fill="var(--ink)"/>
        <ellipse cx="42" cy="7" rx="4.5" ry="6.5" fill="var(--white)"/>
        <ellipse cx="54" cy="7" rx="4.5" ry="6.5" fill="var(--white)"/>
      </svg>
      <p class="gusset-copy">Frisch geröstete Bohnen aus ausgewählten Anbaugebieten, sorgfältig für unser Espresso Event zusammengestellt. Kräftiger Körper, feine Crema und Noten von dunkler Schokolade und gerösteten Nüssen. Ideal für Siebträger und Vollautomaten. Nach dem Öffnen kühl, trocken und lichtgeschützt lagern, um das volle Aroma zu bewahren.</p>
    </div>
  </div>
</section>

<section class="variant variant--metallic">
  <div class="bag">
    <div class="front">
      <div class="brand"><span class="brand-square"></span>KLV Talmetall</div>
      <h1 class="title">ESPRESSO</h1>
      <p class="subtitle">GANZE BOHNE</p>
      <svg class="strength" width="130" height="28" viewBox="0 0 130 28" aria-label="Stärke 3 von 5">
        <ellipse cx="13" cy="14" rx="9" ry="13" fill="var(--gold)"/>
        <ellipse cx="39" cy="14" rx="9" ry="13" fill="var(--gold)"/>
        <ellipse cx="65" cy="14" rx="9" ry="13" fill="var(--gold)"/>
        <ellipse cx="91" cy="14" rx="9" ry="13" fill="var(--white)"/>
        <ellipse cx="117" cy="14" rx="9" ry="13" fill="var(--white)"/>
      </svg>
      <div class="pattern-band" role="img" aria-label="Wabenmuster aus goldenen und silbernen Sechsecken, nach unten ins Schwarz verlaufend"></div>
      <p class="weight">250g</p>
    </div>
    <div class="gusset">
      <div class="brand"><span class="brand-square"></span>KLV Talmetall</div>
      <p class="gusset-title">ESPRESSO</p>
      <p class="gusset-subtitle">GANZE BOHNE</p>
      <svg class="strength" width="50" height="12" viewBox="0 0 60 14" aria-label="Stärke 3 von 5">
        <ellipse cx="6" cy="7" rx="4.5" ry="6.5" fill="var(--ink)"/>
        <ellipse cx="18" cy="7" rx="4.5" ry="6.5" fill="var(--ink)"/>
        <ellipse cx="30" cy="7" rx="4.5" ry="6.5" fill="var(--ink)"/>
        <ellipse cx="42" cy="7" rx="4.5" ry="6.5" fill="var(--white)"/>
        <ellipse cx="54" cy="7" rx="4.5" ry="6.5" fill="var(--white)"/>
      </svg>
      <p class="gusset-copy">Frisch geröstete Bohnen aus ausgewählten Anbaugebieten, sorgfältig für unser Espresso Event zusammengestellt. Kräftiger Körper, feine Crema und Noten von dunkler Schokolade und gerösteten Nüssen. Ideal für Siebträger und Vollautomaten. Nach dem Öffnen kühl, trocken und lichtgeschützt lagern, um das volle Aroma zu bewahren.</p>
    </div>
  </div>
</section>

</body>
</html>
```